Water Well Drilling

Banner will be 2m wide X 4m high. The Banner will be placed on side of road. The application of the banner is for advertising of our water well drilling services. The banner must be designed using two different languages. English and Spanish. The design would be in accordance with our website and Logo designs to maintain the same marketing image. Website www.hondorocaboring.com

```html
<!DOCTYPE html>
<html lang="en">
<head>
<meta charset="utf-8">
<title>Water Well Drilling Banner</title>
<link rel="stylesheet" href="https://fonts.googleapis.com/css2?family=Montserrat:wght@600;700;800&display=swap">
<style>
  :root {
    --navy: #1d3a78;
    --navy-deep: #1a2550;
    --blue-top: #3a5597;
    --blue-mid: #28407c;
    --ink: #18306a;
    --white: #ffffff;
    --page: #e9ebef;
  }
  * { box-sizing: border-box; margin: 0; padding: 0; }
  html, body { width: 1200px; height: 1171px; overflow: hidden; background: var(--page); }
  body { position: relative; font-family: 'Montserrat', sans-serif; }

  .banner {
    position: absolute; left: 331px; top: 20px;
    width: 538px; height: 1131px;
    background: var(--white);
    box-shadow: 0 4px 18px rgba(0,0,0,.18);
    overflow: hidden;
  }

  .section-english {
    position: absolute; left: 0; top: 0; width: 100%; height: 531px;
  }
  .water-backdrop {
    position: absolute; inset: 0;
    background: linear-gradient(180deg, var(--blue-top) 0%, var(--blue-mid) 55%, var(--navy-deep) 100%);
  }
  .headline {
    position: absolute; left: 60px; top: 80px;
    color: var(--white); font-weight: 800;
    font-size: 68px; line-height: 92px; letter-spacing: 0.5px;
  }
  .service-list {
    position: absolute; left: 28px; list-style: none;
    color: var(--white); font-weight: 700; font-size: 22px;
  }
  .service-list li { display: flex; align-items: center; height: 54px; }
  .service-list li::before {
    content: ""; width: 12px; height: 12px; background: var(--white);
    margin-right: 18px; flex: none;
  }
  .section-english .service-list { top: 378px; }

  .contact-band {
    position: absolute; left: 0; top: 531px; width: 100%; height: 216px;
    background: var(--white);
  }
  .brand {
    position: absolute; left: 0; width: 100%; top: 28px;
    display: flex; justify-content: center; align-items: center; gap: 12px;
  }
  .brand-dot { width: 42px; height: 42px; border-radius: 50%; background: var(--navy); }
  .brand-name { color: var(--navy); font-weight: 600; font-size: 21px; line-height: 1; }
  .band-rule {
    position: absolute; left: 0; top: 90px; width: 100%; height: 4px; background: var(--navy);
  }
  .phone {
    position: absolute; left: 30px; top: 112px;
    display: flex; align-items: center; gap: 16px;
    color: var(--ink); font-weight: 800; font-size: 31px; letter-spacing: 1px;
  }
  .email {
    position: absolute; left: 0; width: 100%; top: 170px;
    display: flex; justify-content: center; align-items: center; gap: 14px;
    color: var(--ink); font-weight: 700; font-size: 22px;
  }

  .section-spanish {
    position: absolute; left: 0; top: 747px; width: 100%; height: 384px;
  }
  .section-spanish .water-backdrop {
    background: linear-gradient(180deg, var(--blue-mid) 0%, var(--navy-deep) 60%, #1c2a56 100%);
  }
  .headline-es {
    position: absolute; left: 66px; top: 40px;
    color: var(--white); font-weight: 800; font-size: 50px; line-height: 74px;
  }
  .section-spanish .service-list { top: 200px; left: 45px; font-size: 22px; }
  .section-spanish .service-list li { height: auto; align-items: flex-start; margin-bottom: 14px; line-height: 34px; }
  .section-spanish .service-list li::before { margin-top: 11px; margin-right: 12px; }
</style>
</head>
<body>
  <main class="banner">
    <section class="section-english">
      <div class="water-backdrop" role="img" aria-label="Deep blue water surface with splashing droplets"></div>
      <h1 class="headline">WATER<br>WELL<br>DRILLING</h1>
      <ul class="service-list">
        <li>PERMITS AND CONCESSIONS</li>
        <li>PUMP INSTALL AND REPAIR</li>
      </ul>
    </section>

    <section class="contact-band">
      <div class="brand">
        <span class="brand-dot"></span>
        <span class="brand-name">Perforaciones Hondo Roca</span>
      </div>
      <div class="band-rule"></div>
      <p class="phone">
        <svg width="34" height="40" viewBox="0 0 24 28" aria-hidden="true">
          <path fill="var(--ink)" d="M5 1 L9 1 L11 8 L8 10 C9 15 11 19 15 22 L18 19 L23 22 L22 27 C12 27 2 16 2 5 Z"/>
        </svg>
        2460 7100/8791 3322
      </p>
      <p class="email">
        <svg width="26" height="18" viewBox="0 0 26 18" aria-hidden="true">
          <rect x="1" y="1" width="24" height="16" fill="none" stroke="var(--ink)" stroke-width="2"/>
          <path d="M1 1 L13 10 L25 1 M1 17 L10 8 M25 17 L16 8" fill="none" stroke="var(--ink)" stroke-width="2"/>
        </svg>
        Info@hondorocaboring.com
      </p>
    </section>

    <section class="section-spanish">
      <div class="water-backdrop" role="img" aria-label="Dark blue water texture"></div>
      <h2 class="headline-es">PERFORACIÓN<br>DE POZOS</h2>
      <ul class="service-list">
        <li>PERMISOS Y CONCESIONES</li>
        <li>INSTALACIÓN Y REPARACIÓN<br>DE BOMBAS</li>
      </ul>
    </section>
  </main>
</body>
</html>
```